Modern Business Card for Larkwell 2018

Our company assumes the best about people. We are creating an online community of entrepreneurs and business leaders who struggle with marketing their business online.

This business card should POP! We recently got a new logo and are launching a new website next month, so our business cards should make a statement that feels:
-Fresh
-Smart
-Trustworthy
-Fun

Target Market(s)

small business owners, entrepreneurs

Industry/Entity Type

Digital Marketing

Contact Information for Business Card

Dimensions: 3.5" x 2"

Font styles to use
Sans Serif

Colors
f37122
ffffff

Requirements
Must have
• We need a business card with a modern, bold design. We will use one side of the card as a lead-generation offer, so text on one side will need to fit up to 140 characters. The business card should stick to our core colors (orange, black, and white).
Nice to have
• We think a vertical "portrait" design could be interesting.
Should not have
• Should not look like a traditional business card. The round icon should stand out from a distance.

```html
<!DOCTYPE html>
<html lang="en">
<head>
<meta charset="utf-8">
<title>Larkwell Business Card</title>
<link rel="stylesheet" href="https://fonts.googleapis.com/css2?family=Barlow:wght@400;500;700;800&family=Merriweather:ital,wght@1,900&display=swap">
<style>
  :root {
    --orange: #f37122;
    --white: #ffffff;
    --charcoal: #333333;
    --ink: #222222;
    --text-grey: #3a3a3a;
    --backdrop: #e6e6e6;
  }
  html, body {
    margin: 0;
    width: 1200px;
    height: 1200px;
    overflow: hidden;
    background: var(--backdrop);
  }
  .canvas {
    position: relative;
    width: 1200px;
    height: 1200px;
  }
  .card {
    position: absolute;
    left: 219px;
    width: 761px;
    height: 435px;
    display: block;
    box-shadow: 0 18px 30px rgba(0,0,0,0.25);
  }
  .card--front { top: 102px; }
  .card--back { top: 627px; }

  .holder-name {
    font-family: "Barlow", sans-serif;
    font-weight: 800;
    font-size: 52px;
    letter-spacing: 1px;
    fill: var(--ink);
  }
  .holder-role {
    font-family: "Barlow", sans-serif;
    font-weight: 500;
    font-size: 29px;
    fill: var(--text-grey);
  }
  .holder-email {
    font-family: "Barlow", sans-serif;
    font-weight: 400;
    font-size: 33px;
    fill: var(--text-grey);
  }
  .promise {
    font-family: "Barlow", sans-serif;
    font-weight: 500;
    font-size: 42px;
    fill: var(--white);
  }
  .brand-name {
    font-family: "Barlow", sans-serif;
    font-weight: 700;
    font-size: 92px;
    fill: var(--white);
  }
  .brand-tagline {
    font-family: "Merriweather", serif;
    font-style: italic;
    font-weight: 900;
    font-size: 27px;
    fill: var(--white);
  }
  .offer {
    font-family: "Barlow", sans-serif;
    font-weight: 500;
    font-size: 26px;
    fill: var(--white);
  }
  .offer-url {
    font-family: "Barlow", sans-serif;
    font-weight: 500;
    font-size: 40px;
    fill: var(--white);
  }
</style>
</head>
<body>
<main class="canvas">

  <svg class="card card--front" viewBox="0 0 945 540" xmlns="http://www.w3.org/2000/svg" aria-label="Card front">
    <defs>
      <clipPath id="front-clip"><rect width="945" height="540"/></clipPath>
    </defs>
    <rect class="front-base" width="945" height="540" fill="var(--white)"/>
    <g clip-path="url(#front-clip)">
      <circle class="front-arc" cx="800" cy="250" r="434" fill="var(--orange)"/>
      <rect class="front-fill" x="800" y="0" width="145" height="540" fill="var(--orange)"/>
    </g>
    <text class="holder-name" x="58" y="340">DANA</text>
    <text class="holder-name" x="56" y="405">WHITFIELD</text>
    <text class="holder-role" x="46" y="452">Story Marketing Coach</text>
    <text class="holder-email" x="46" y="493">dana@larkwellnow.com</text>
  </svg>

  <svg class="card card--back" viewBox="0 0 945 540" xmlns="http://www.w3.org/2000/svg" aria-label="Card back">
    <rect class="band band--top" x="0" y="0" width="945" height="189" fill="var(--charcoal)"/>
    <rect class="band band--brand" x="0" y="189" width="945" height="225" fill="var(--orange)"/>
    <rect class="band band--offer" x="0" y="414" width="945" height="126" fill="var(--charcoal)"/>

    <text class="promise" x="472" y="64" text-anchor="middle">REACH MORE PEOPLE.</text>
    <text class="promise" x="472" y="114" text-anchor="middle">MAKE MORE MONEY.</text>
    <text class="promise" x="472" y="164" text-anchor="middle">CREATE MORE IMPACT.</text>

    <circle class="brand-dot" cx="472" cy="238" r="22" fill="var(--white)"/>
    <text class="brand-name" x="472" y="358" text-anchor="middle">LARKWELL</text>
    <text class="brand-tagline" x="472" y="395" text-anchor="middle">Tell Stories That Inspire Action</text>

    <text class="offer" x="472" y="458" text-anchor="middle">Get your free Larkwell Starter Package and our marketing guide today at</text>
    <text class="offer-url" x="472" y="498" text-anchor="middle">larkwellnow.com/start</text>
  </svg>

</main>
</body>
</html>
```